MTSS Pyramid graphic needed for use in presentations and on my website

I am a consultant and need graphics to represent the MTSS pyramid (educational terminology) for use on my website and in slide decks. I've included documentation below that shows the MTSS pyramid, some preferences I have thought of, and my color palette. The MTSS pyramid is well-known in my field and I'd like one that I can use in all my presentations and on my website that looks professional and modern.

Target Market(s)

Educational leaders and educators

Industry/Entity Type

Educational Consulting

Font styles to use
Serif
Sans Serif

Colors
00AB8E
00BBA5
67D7C9
C6EFE9
E9F9F6
6B429C
8869AF
B7A5CE
E3DAEB
F3F0F8

Requirements
Must have
• a pyramid that can be recognized as an MTSS pyramid, use of colors that align with my color palette, a professional, modern look and feel, 3 sections with the largest at the bottom of the pyramid
Nice to have
• rounded corners, maybe 3D
Should not have
• a pyramid in a different shape or orientation, any more or fewer than 3 sections

```html
<!DOCTYPE html>
<html lang="en">
<head>
<meta charset="utf-8">
<title>MTSS Pyramid Graphic</title>
<link rel="stylesheet" href="https://fonts.googleapis.com/css2?family=Montserrat:ital,wght@0,600;0,700;1,800&display=swap">
<style>
  :root {
    --teal-700: #00AB8E;
    --teal-600: #00BBA5;
    --teal-400: #67D7C9;
    --teal-200: #C6EFE9;
    --teal-100: #E9F9F6;
    --purple-700: #6B429C;
    --purple-600: #8869AF;
    --purple-400: #B7A5CE;
    --purple-200: #E3DAEB;
    --purple-100: #F3F0F8;
    --ink: #111111;
    --white: #FFFFFF;
  }
  html, body {
    margin: 0;
    padding: 0;
    width: 1200px;
    height: 1200px;
    overflow: hidden;
    background: var(--white);
  }
  .sheet { display: block; width: 1200px; height: 1200px; }
  .panel { fill: var(--teal-100); }
  .tier { stroke-width: 12; stroke-linejoin: round; }
  .teal-700 { fill: var(--teal-700); stroke: var(--teal-700); }
  .teal-600 { fill: var(--teal-600); stroke: var(--teal-600); }
  .teal-400 { fill: var(--teal-400); stroke: var(--teal-400); }
  .purple-400 { fill: var(--purple-400); stroke: var(--purple-400); }
  .purple-200 { fill: var(--purple-200); stroke: var(--purple-200); }
  .gap-teal { fill: var(--teal-200); }
  .gap-purple { fill: var(--purple-100); }
  .tier-label {
    font-family: 'Montserrat', sans-serif;
    font-weight: 600;
    fill: var(--white);
    text-anchor: middle;
  }
  .tier-label.t1 { font-size: 44px; }
  .tier-label.t2 { font-size: 30px; }
  .tier-label.t3 { font-size: 14px; }
  .caption {
    font-family: 'Montserrat', sans-serif;
    font-weight: 700;
    font-size: 20px;
    letter-spacing: 0.3px;
    fill: var(--ink);
  }
  .caption.centered { text-anchor: middle; }
  .title-block { fill: var(--purple-700); }
  .title {
    font-family: 'Montserrat', sans-serif;
    font-style: italic;
    font-weight: 800;
    font-size: 150px;
    fill: var(--white);
    letter-spacing: -2px;
  }
</style>
</head>
<body>
<svg class="sheet" viewBox="0 0 1932 1932" xmlns="http://www.w3.org/2000/svg" xmlns:xlink="http://www.w3.org/1999/xlink" role="img" aria-label="MTSS pyramid graphic set with colour palette">
  <defs>
    <path id="tier-3" d="M0,8 L49,82 L-49,82 Z"/>
    <path id="tier-2" d="M-66,118 L66,118 L104,178 L-104,178 Z"/>
    <path id="tier-1" d="M-122,214 L122,214 L192,336 L-192,336 Z"/>
    <path id="tier-gap" d="M-58,88 L58,88 L128,208 L-128,208 Z"/>
  </defs>

  <!-- Row 1 -->
  <rect class="panel" x="2" y="0" width="463" height="463"/>
  <rect class="panel" x="483" y="0" width="463" height="463"/>
  <rect class="panel" x="960" y="0" width="463" height="463"/>
  <!-- Row 2 -->
  <rect class="panel" x="2" y="478" width="463" height="463"/>
  <rect class="panel" x="483" y="478" width="463" height="463"/>
  <rect class="panel" x="960" y="478" width="463" height="463"/>
  <!-- Row 3 -->
  <rect class="panel" x="2" y="962" width="463" height="463"/>
  <rect class="panel" x="483" y="962" width="463" height="463"/>
  <!-- Row 4 -->
  <rect class="panel" x="2" y="1469" width="463" height="463"/>
  <rect class="panel" x="483" y="1469" width="463" height="463"/>

  <!-- Full labels -->
  <g class="pyramid" transform="translate(231,45)">
    <use href="#tier-gap" class="gap-teal"/>
    <use href="#tier-3" class="tier teal-400"/>
    <use href="#tier-2" class="tier teal-600"/>
    <use href="#tier-1" class="tier teal-700"/>
    <text class="tier-label t3" x="0" y="62">Tier 3</text>
    <text class="tier-label t2" x="0" y="157">Tier 2</text>
    <text class="tier-label t1" x="0" y="285">Tier 1</text>
  </g>
  <text class="caption centered" x="233" y="428">Pyramid with Tier 1, Tier 2, Tier 3 labels</text>

  <!-- No labels -->
  <g class="pyramid" transform="translate(714,45)">
    <use href="#tier-gap" class="gap-teal"/>
    <use href="#tier-3" class="tier teal-400"/>
    <use href="#tier-2" class="tier teal-600"/>
    <use href="#tier-1" class="tier teal-700"/>
  </g>
  <text class="caption centered" x="729" y="423">Pyramid without labels</text>

  <!-- Tier 2/3 with label -->
  <g class="pyramid" transform="translate(1194,45)">
    <use href="#tier-gap" class="gap-purple"/>
    <use href="#tier-3" class="tier teal-600"/>
    <use href="#tier-2" class="tier teal-700"/>
    <use href="#tier-1" class="tier purple-400"/>
    <text class="tier-label t3" x="0" y="62">Tier 3</text>
    <text class="tier-label t2" x="0" y="157">Tier 2</text>
  </g>
  <text class="caption" x="1017" y="423">Pyramid with Tier 2/3 highlighted</text>
  <text class="caption" x="1017" y="447">with the label</text>

  <!-- Tier 1 with label -->
  <g class="pyramid" transform="translate(231,520)">
    <use href="#tier-gap" class="gap-purple"/>
    <use href="#tier-3" class="tier purple-200"/>
    <use href="#tier-2" class="tier purple-400"/>
    <use href="#tier-1" class="tier teal-700"/>
    <text class="tier-label t1" x="0" y="285">Tier 1</text>
  </g>
  <text class="caption" x="72" y="902">Pyramid with Tier 1 highlighted</text>
  <text class="caption" x="72" y="925">with the label</text>

  <!-- Tier 1 without label -->
  <g class="pyramid" transform="translate(714,503)">
    <use href="#tier-gap" class="gap-purple"/>
    <use href="#tier-3" class="tier purple-200"/>
    <use href="#tier-2" class="tier purple-400"/>
    <use href="#tier-1" class="tier teal-700"/>
  </g>
  <text class="caption" x="547" y="900">Pyramid with Tier 1 highlighted</text>
  <text class="caption" x="547" y="923">without the label</text>

  <!-- Tier 2/3 without label -->
  <g class="pyramid" transform="translate(1194,516)">
    <use href="#tier-gap" class="gap-purple"/>
    <use href="#tier-3" class="tier teal-600"/>
    <use href="#tier-2" class="tier teal-700"/>
    <use href="#tier-1" class="tier purple-400"/>
  </g>
  <text class="caption" x="1017" y="902">Pyramid with Tier 2/3 highlighted</text>
  <text class="caption" x="1017" y="925">without the label</text>

  <!-- Tier 2 with label -->
  <g class="pyramid" transform="translate(231,994)">
    <use href="#tier-gap" class="gap-purple"/>
    <use href="#tier-3" class="tier purple-200"/>
    <use href="#tier-2" class="tier teal-700"/>
    <use href="#tier-1" class="tier purple-400"/>
    <text class="tier-label t2" x="0" y="157">Tier 2</text>
  </g>
  <text class="caption" x="72" y="1380">Pyramid with Tier 2 highlighted</text>
  <text class="caption" x="72" y="1403">with the label</text>

  <!-- Tier 2 without label -->
  <g class="pyramid" transform="translate(714,994)">
    <use href="#tier-gap" class="gap-purple"/>
    <use href="#tier-3" class="tier purple-200"/>
    <use href="#tier-2" class="tier teal-700"/>
    <use href="#tier-1" class="tier purple-400"/>
  </g>
  <text class="caption" x="547" y="1375">Pyramid with Tier 2 highlighted</text>
  <text class="caption" x="547" y="1398">without the label</text>

  <!-- Tier 3 with label -->
  <g class="pyramid" transform="translate(233,1508)">
    <use href="#tier-gap" class="gap-purple"/>
    <use href="#tier-3" class="tier teal-700"/>
    <use href="#tier-2" class="tier purple-200"/>
    <use href="#tier-1" class="tier purple-400"/>
    <text class="tier-label t3" x="0" y="62">Tier 3</text>
  </g>
  <text class="caption" x="72" y="1895">Pyramid with Tier 3 highlighted</text>
  <text class="caption" x="72" y="1918">with the label</text>

  <!-- Tier 3 without label -->
  <g class="pyramid" transform="translate(707,1508)">
    <use href="#tier-gap" class="gap-purple"/>
    <use href="#tier-3" class="tier teal-700"/>
    <use href="#tier-2" class="tier purple-200"/>
    <use href="#tier-1" class="tier purple-400"/>
  </g>
  <text class="caption" x="547" y="1895">Pyramid with Tier 3 highlighted</text>
  <text class="caption" x="547" y="1918">without the label</text>

  <!-- Palette -->
  <g class="palette">
    <rect x="1555" y="52" width="109" height="141" fill="var(--purple-700)"/>
    <rect x="1555" y="235" width="109" height="141" fill="var(--purple-600)"/>
    <rect x="1555" y="418" width="109" height="141" fill="var(--purple-400)"/>
    <rect x="1555" y="601" width="109" height="141" fill="var(--purple-200)"/>
    <rect x="1555" y="785" width="109" height="141" fill="var(--purple-100)"/>
    <rect x="1713" y="52" width="109" height="141" fill="var(--teal-700)"/>
    <rect x="1713" y="235" width="109" height="141" fill="var(--teal-600)"/>
    <rect x="1713" y="418" width="109" height="141" fill="var(--teal-400)"/>
    <rect x="1713" y="601" width="109" height="141" fill="var(--teal-200)"/>
    <rect x="1713" y="785" width="109" height="141" fill="var(--teal-100)"/>
  </g>

  <!-- Title block -->
  <rect class="title-block" x="1017" y="1057" width="915" height="875"/>
  <text class="title" x="1138" y="1375">MTSS</text>
  <text class="title" x="1138" y="1550">Pyramid</text>
  <text class="title" x="1138" y="1725">Graphic</text>
</svg>
</body>
</html>
```